Book Cover - needed: frontpage Authors Name: Greta Hollmann Title: Nebelgrund size of page: 14,8x21cm, thickness 3cm, pages 460 I need a book cover. Book is in German, called "Nebelgrund" All which is something like "The four of us" in english. It is a novel. Page is 14,8x21cm, 460pages. Novel is on four young people, the medical student Sabine with difficulties walking is getting to know a neurosurgeon Uwe. He is mute, captured n speechlessness and sorrow. At the sametime Florian is interested in Sabine and his sister Ilse, a friend of Sabine, makes advances to Uwe. Uwe and Sabine are inseparable. At unconventionel question comes up: maybe They Could start into life being a pair of four, instead of starting on into insoluble competition? This novel is Followed by two more books. In the second "road past the orchard" Uwe and Sabine leave Germany and go to Boston for six months "Walk by the harbor". The third book "Under the lanterns" Uwe very slowly Allows people to enter to his life. Sabine battles to get him out of his loneliness and speechlesness "She waits by rivers". For the first book I imagine a cover with four faces, maybe in four triangles each with one face. Faces must not be very clear or exact, a big lettered "4" could be before the faces. Sabine is Described as having long dark hair and dark eyes, small, with cruches for her walking diffculties. She is friendly, smiling, open-minded, communicative. Uwe so dark haired, extremely slim, sad, serious, timid, desperate and mute. His mouth Could be missing. Florian has fair hair, he is a musician, violinist, loves his music, one Could draw him with a little friendly smile. He is ready to help everyone, but a little shy. Ilse, his sister, long fair hair, funny, lovely, uncomplicated, Sabine's best friend. More open and active than her brother. What they like to do together is music. They play in the same orchestra. Sabine and Florian violin. Ilse Flute. Uwe clarinet. Uwe is therefore a great pianist and dedicated surgeon, highly intelligent, but lonesome. Hope I have written enough about the characters foryou to get the faces "right". Another idea than faces Could be four people in a little sailing boat - it is one of the central scenes.

```html
<!DOCTYPE html>
<html lang="en">
<head>
<meta charset="utf-8">
<title>Nebelgrund – Book Cover</title>
<link rel="stylesheet" href="https://fonts.googleapis.com/css2?family=Jost:ital,wght@0,300;0,400;0,600;1,300&display=swap">
<style>
  :root {
    --stage: #c0c0c0;
    --teal: #508580;
    --gold: #c8b86c;
    --ink: #222222;
    --paper: #ffffff;
    --font: "Jost", "Futura", sans-serif;
  }
  html, body {
    margin: 0;
    width: 1200px;
    height: 808px;
    overflow: hidden;
    background: var(--stage);
    font-family: var(--font);
  }
  .stage {
    position: absolute;
    left: 0;
    top: 0;
    width: 1096px;
    height: 738px;
    transform: scale(1.09489);
    transform-origin: 0 0;
  }
  .cover-art {
    position: absolute;
    left: 0;
    top: 0;
    width: 1096px;
    height: 738px;
  }
  .abstract {
    position: absolute;
    left: 97px;
    top: 80px;
    width: 379px;
    margin: 0;
    color: var(--paper);
    font-weight: 300;
    font-style: italic;
    font-size: 17.4px;
    line-height: 22.4px;
    text-align: justify;
    hyphens: manual;
  }
  .abstract p { margin: 0; }
  .abstract .label { text-transform: uppercase; text-align: left; }
  .back-author {
    position: absolute;
    right: 620px;
    top: 518px;
    color: var(--paper);
    font-weight: 300;
    font-style: italic;
    font-size: 17.4px;
  }
  .editor-note {
    position: absolute;
    left: 116px;
    top: 636px;
    color: var(--ink);
    font-weight: 400;
    font-size: 17px;
    letter-spacing: 1.1px;
    text-transform: uppercase;
  }
  .spine-text {
    position: absolute;
    left: 542px;
    color: var(--gold);
    transform: rotate(90deg);
    transform-origin: 0 0;
    white-space: nowrap;
    line-height: 1;
  }
  .spine-author {
    top: 150px;
    font-weight: 300;
    font-style: italic;
    font-size: 17px;
    margin-left: 9px;
  }
  .spine-title {
    top: 410px;
    font-weight: 600;
    font-size: 20px;
    margin-left: 11px;
  }
  .front-title {
    position: absolute;
    left: 596px;
    width: 416px;
    top: 80px;
    margin: 0;
    text-align: center;
    color: var(--ink);
    font-weight: 400;
    font-size: 44px;
    letter-spacing: 0.5px;
  }
  .front-author {
    position: absolute;
    left: 706px;
    width: 200px;
    top: 647px;
    text-align: center;
    color: var(--ink);
    font-weight: 400;
    font-size: 18px;
  }
</style>
</head>
<body>
<main class="stage">
  <svg class="cover-art" viewBox="0 0 1096 738" aria-hidden="false">
    <!-- back cover -->
    <rect class="back-panel" x="62" y="62" width="430" height="619" fill="var(--teal)"/>
    <polygon class="back-footer" points="62,505 492,610 492,681 62,681" fill="var(--paper)"/>

    <!-- spine -->
    <rect class="spine" x="492" y="62" width="104" height="619" fill="var(--ink)"/>
    <rect class="spine-rule" x="495" y="62" width="1.2" height="619" fill="#cfcfcf"/>
    <rect class="spine-rule" x="591" y="62" width="1.2" height="619" fill="#cfcfcf"/>
    <rect class="spine-rule" x="497" y="607" width="94" height="1.5" fill="#cfcfcf"/>
    <polygon class="spine-facet" points="497,610 588,610 542,645" fill="var(--paper)"/>
    <polygon class="spine-facet" points="497,610 542,645 497,681" fill="var(--teal)"/>
    <polygon class="spine-facet" points="588,610 588,681 542,645" fill="var(--gold)"/>

    <!-- front cover -->
    <rect class="front-panel" x="596" y="62" width="428" height="619" fill="var(--paper)"/>
    <polygon class="front-facet" points="596,62 1008,62 805,400 596,125" fill="var(--gold)"/>
    <polygon class="front-facet" points="1008,62 1024,62 1024,681 805,400" fill="var(--ink)"/>
    <polygon class="front-facet" points="805,400 1024,681 636,681" fill="var(--teal)"/>

    <!-- character portrait areas -->
    <rect class="portrait" role="img" aria-label="Head silhouette of the dark-haired young man" x="752" y="175" width="80" height="135" rx="34" fill="var(--teal)"/>
    <rect class="portrait" role="img" aria-label="Head silhouette of the young woman with long curly dark hair" x="600" y="328" width="160" height="165" rx="60" fill="var(--ink)"/>
    <rect class="portrait" role="img" aria-label="Head silhouette of the young woman with long fair hair" x="887" y="332" width="113" height="155" rx="50" fill="var(--paper)"/>
    <rect class="portrait" role="img" aria-label="Head silhouette of the fair-haired young musician" x="762" y="483" width="100" height="139" rx="38" fill="var(--gold)"/>
  </svg>

  <section class="abstract">
    <p class="label">Example abstract</p>
    <p>Novel is on four young people, the medical student Sabine with difficulties walking is getting to know a neurosurgeon Uwe. He is mute, captured n speechlessness and sorrow. At the same time Florian is interested in Sabine and his sister Ilse, a friend of Sabine, makes advances to Uwe. Uwe and Sabine are inseparable. An uncon&shy;ventionel question comes up: maybe they could start into life being a pair of four, instead of starting into an insoluble competition?</p>
    <p>This novel is followed by two more books. In the second "road past the orchard" Uwe and Sabine leave Germany and go to Boston for six months "Walk by the harbor". The third book "Under the lanterns" Uwe very slowly allows people to enter to his life. Sabine battles to get him out of his loneliness and speechlesness "She waits by rivers".</p>
  </section>
  <div class="back-author">Greta Hollmann</div>
  <div class="editor-note">Space for your editor / editor text</div>

  <div class="spine-text spine-author">Greta Hollmann</div>
  <div class="spine-text spine-title">Nebelgrund</div>

  <h1 class="front-title">Nebelgrund</h1>
  <div class="front-author">Greta Hollmann</div>
</main>
</body>
</html>
```